PowerPoint Master for IT company (lumoGrid GmbH)

As IT company we work in the fields Mobile, Big Data, Predictive Maintenance, Industry 4.0 and Data Science for the german Rail company "Nordwerk Schiene". We already have a Logo, coloring and a website (Attached Files).

What we need is a clear, professional and simple Design (nothing fancy) for PowerPoint/Word Master and Business Cards. Stockphotos from https://bildarchiv.nordwerkschiene.example/ can be used beside the attached logos.

We are a german company but would need either an universal or DE and EN template for PoerPoint.

Target Market(s)

IT, B2B, Rail companies, Industry

Contact Information for Business Card

- Logo
- Company Name
- Name
- Position
- Address
- Phone
- Mail

Font styles to use
Sans Serif

```html
<!DOCTYPE html>
<html lang="en">
<head>
<meta charset="utf-8">
<title>lumoGrid – Slide Master Layouts</title>
<link href="https://fonts.googleapis.com/css2?family=Roboto:wght@400;500;700&display=swap" rel="stylesheet">
<style>
  :root {
    --canvas: #ececec;
    --paper: #ffffff;
    --ink: #262626;
    --muted: #7a7a7a;
    --rule: #e2e2e2;
    --navy: #1c1f5a;
    --blue: #2b3e84;
    --pale: #e3e6f0;
    --photo-a: #c9c2b4;
    --photo-b: #5a5752;
  }
  * { box-sizing: border-box; margin: 0; padding: 0; }
  html, body { width: 1200px; height: 1050px; overflow: hidden; }
  body { background: var(--canvas); font-family: "Roboto", Arial, sans-serif; color: var(--ink); position: relative; }

  .slide { position: absolute; width: 517px; height: 291px; background: var(--paper); overflow: hidden; }
  .col-left { left: 67px; }
  .col-right { left: 615px; width: 516px; }
  .row-1 { top: 69px; }
  .row-2 { top: 379px; }
  .row-3 { top: 690px; width: 517px; height: 294px; }

  .slide-title { position: absolute; left: 16px; top: 20px; font-size: 18px; font-weight: 400; letter-spacing: 0.1px; }
  .title-rule { position: absolute; left: 16px; right: 16px; top: 45px; height: 1px; background: var(--rule); }
  .page-number { position: absolute; right: 16px; top: 15px; font-size: 6px; }
  .subtitle { position: absolute; left: 16px; top: 50px; font-size: 8px; }
  .block-heading { position: absolute; font-size: 9px; font-weight: 700; }

  .bullets { position: absolute; list-style: none; font-size: 8px; line-height: 15.8px; }
  .bullets li { position: relative; padding-left: 7px; }
  .bullets li::before { content: "•"; position: absolute; left: 0; font-size: 6px; }
  .bullets .l2 { margin-left: 8px; }
  .bullets .l3 { margin-left: 16px; }
  .bullets .l4 { margin-left: 24px; }

  .photo-slot { position: absolute; left: 267px; top: 58px; width: 234px; height: 197px;
    background: linear-gradient(120deg, var(--photo-a) 0%, #e9e4da 40%, var(--photo-b) 100%); }

  .chart { position: absolute; left: 0; top: 0; }

  .footer { position: absolute; left: 0; right: 0; bottom: 0; height: 21px; background: var(--navy); color: #fff; }
  .partner { position: absolute; left: 16px; top: 5px; }
  .partner-box { display: block; width: 7px; height: 5px; background: #fff; }
  .partner-name { display: block; font-size: 3px; margin-top: 2px; white-space: nowrap; }
  .brand { position: absolute; right: 16px; top: 6px; display: flex; align-items: center; gap: 3px; font-size: 7px; font-weight: 500; letter-spacing: 0.4px; }
  .brand-dot { width: 9px; height: 9px; border-radius: 50%; background: #fff; }
</style>
</head>
<body>

<!-- Text -->
<section class="slide col-left row-1">
  <h1 class="slide-title">Slide with text</h1>
  <div class="title-rule"></div>
  <ul class="bullets" style="left:16px;top:55px">
    <li>Place text here</li><li class="l2">Place text here</li><li class="l3">Place text here</li><li class="l4">Place text here</li>
  </ul>
  <footer class="footer"><div class="partner"><span class="partner-box"></span><span class="partner-name">Nordwerk Engineering &amp; Consulting</span></div><div class="brand">LUMOGRID<span class="brand-dot"></span></div></footer>
</section>

<!-- Text with subtitle -->
<section class="slide col-right row-1">
  <span class="page-number">15</span>
  <h1 class="slide-title">Slide with text</h1>
  <div class="title-rule"></div>
  <p class="subtitle">Subtitle</p>
  <footer class="footer"><div class="partner"><span class="partner-box"></span><span class="partner-name">Nordwerk Engineering &amp; Consulting</span></div><div class="brand">LUMOGRID<span class="brand-dot"></span></div></footer>
</section>

<!-- Text and image -->
<section class="slide col-left row-2">
  <h1 class="slide-title">Slide with text and image</h1>
  <div class="title-rule"></div>
  <ul class="bullets" style="left:16px;top:55px">
    <li>Place text here</li><li class="l2">Place text here</li><li class="l3">Place text here</li><li class="l4">Place text here</li>
  </ul>
  <div class="photo-slot" role="img" aria-label="Stock photo: colleagues talking in a bright office"></div>
  <footer class="footer"><div class="partner"><span class="partner-box"></span><span class="partner-name">Nordwerk Engineering &amp; Consulting</span></div><div class="brand">LUMOGRID<span class="brand-dot"></span></div></footer>
</section>

<!-- Text and chart -->
<section class="slide col-right row-2">
  <h1 class="slide-title">Slide with text and chart</h1>
  <div class="title-rule"></div>
  <h2 class="block-heading" style="left:16px;top:64px">Title place holder</h2>
  <ul class="bullets" style="left:16px;top:82px">
    <li>Place text here</li><li class="l2">Place text here</li><li class="l3">Place text here</li><li class="l4">Place text here</li>
  </ul>
  <svg class="chart" width="516" height="291" viewBox="0 0 516 291" font-family="Roboto, Arial, sans-serif">
    <text x="382" y="71" font-size="9" fill="#555" text-anchor="middle">Chart Title</text>
    <g stroke="#e6e6e6" stroke-width="0.6">
      <line x1="282" y1="80" x2="495" y2="80"/><line x1="282" y1="104.3" x2="495" y2="104.3"/>
      <line x1="282" y1="128.7" x2="495" y2="128.7"/><line x1="282" y1="153" x2="495" y2="153"/>
      <line x1="282" y1="177.3" x2="495" y2="177.3"/><line x1="282" y1="201.7" x2="495" y2="201.7"/>
    </g>
    <line x1="282" y1="226" x2="495" y2="226" stroke="#cfcfcf" stroke-width="0.6"/>
    <g font-size="5.5" fill="#666" text-anchor="end">
      <text x="272" y="82">6</text><text x="272" y="106">5</text><text x="272" y="131">4</text>
      <text x="272" y="155">3</text><text x="272" y="179">2</text><text x="272" y="204">1</text><text x="272" y="228">0</text>
    </g>
    <g fill="var(--blue)">
      <rect x="288" y="121.5" width="9" height="104.5"/><rect x="342" y="165.2" width="9" height="60.8"/>
      <rect x="396" y="140.9" width="9" height="85.1"/><rect x="450" y="116.6" width="9" height="109.4"/>
    </g>
    <g fill="var(--navy)">
      <rect x="300" y="167.7" width="9" height="58.3"/><rect x="354" y="119" width="9" height="107"/>
      <rect x="408" y="182.2" width="9" height="43.8"/><rect x="462" y="158" width="9" height="68"/>
    </g>
    <g fill="var(--pale)">
      <rect x="312" y="177.3" width="9" height="48.7"/><rect x="366" y="177.3" width="9" height="48.7"/>
      <rect x="420" y="153" width="9" height="73"/><rect x="474" y="104.3" width="9" height="121.7"/>
    </g>
    <g font-size="5.5" fill="#666" text-anchor="middle">
      <text x="304" y="236">Category 1</text><text x="358" y="236">Category 2</text>
      <text x="412" y="236">Category 3</text><text x="466" y="236">Category 4</text>
    </g>
    <g font-size="5.5" fill="#666">
      <rect x="335" y="244" width="3" height="3" fill="var(--blue)"/><text x="340" y="248">Series 1</text>
      <rect x="370" y="244" width="3" height="3" fill="var(--navy)"/><text x="375" y="248">Series 2</text>
      <rect x="404" y="244" width="3" height="3" fill="var(--pale)"/><text x="409" y="248">Series 3</text>
    </g>
  </svg>
  <footer class="footer"><div class="partner"><span class="partner-box"></span><span class="partner-name">Nordwerk Engineering &amp; Consulting</span></div><div class="brand">LUMOGRID<span class="brand-dot"></span></div></footer>
</section>

<!-- Two columns -->
<section class="slide col-left row-3">
  <h1 class="slide-title">Place text here</h1>
  <div class="title-rule"></div>
  <h2 class="block-heading" style="left:16px;top:64px">Place text here</h2>
  <ul class="bullets" style="left:16px;top:82px">
    <li>Place text here</li><li class="l2">Place text here</li><li class="l3">Place text here</li><li class="l4">Place text here</li>
  </ul>
  <h2 class="block-heading" style="left:267px;top:64px">Place text here</h2>
  <ul class="bullets" style="left:267px;top:82px">
    <li>Place text here</li><li class="l2">Place text here</li><li class="l3">Place text here</li><li class="l4">Place text here</li>
  </ul>
  <footer class="footer"><div class="partner"><span class="partner-box"></span><span class="partner-name">Nordwerk Engineering &amp; Consulting</span></div><div class="brand">LUMOGRID<span class="brand-dot"></span></div></footer>
</section>

<!-- Three columns -->
<section class="slide col-right row-3">
  <div class="title-rule"></div>
  <ul class="bullets" style="left:16px;top:175px">
    <li>Place text here</li><li class="l2">Place text here</li><li class="l3">Place text here</li><li class="l4">Place text here</li>
  </ul>
  <ul class="bullets" style="left:179px;top:175px">
    <li>Place text here</li><li class="l2">Place text here</li><li class="l3">Place text here</li><li class="l4">Place text here</li>
  </ul>
  <ul class="bullets" style="left:342px;top:175px">
    <li>Place text here</li><li class="l2">Place text here</li><li class="l3">Place text here</li><li class="l4">Place text here</li>
  </ul>
  <footer class="footer"><div class="partner"><span class="partner-box"></span><span class="partner-name">Nordwerk Engineering &amp; Consulting</span></div><div class="brand">LUMOGRID<span class="brand-dot"></span></div></footer>
</section>

</body>
</html>
```